We need a business card design for an assisted living facility in Los Angeles. We have a logo selected but we would like a business card design that will leave a lasting impression on families looking to place their elderly loved ones in our care as well as on other facility providers who may refer their elderly residents to our facility.

```html
<!DOCTYPE html>
<html lang="en">
<head>
<meta charset="utf-8">
<title>Ashford Crest Senior Living — Business Card</title>
<link href="https://fonts.googleapis.com/css2?family=Open+Sans:wght@400;600;700&display=swap" rel="stylesheet">
<style>
  :root {
    --backdrop: #cdcdcd;
    --card-white: #ffffff;
    --brand-blue: #0f72bd;
    --accent-grey: #8a8a8a;
    --ink: #1d1d1d;
    --photo-deep: #3f6597;
    --photo-mid: #5b80b0;
    --photo-light: #7f9cc2;
  }
  * { margin: 0; padding: 0; box-sizing: border-box; }
  html, body {
    width: 1146px; height: 1200px; overflow: hidden;
    background: var(--backdrop);
    font-family: "Open Sans", Arial, sans-serif;
  }
  .canvas { position: relative; width: 1146px; height: 1200px; }
  .card {
    position: absolute; left: 235px; width: 680px; height: 392px; overflow: hidden;
  }
  .card-front { top: 145px; background: var(--card-white); }
  .card-back { top: 623px; }

  .brand-name {
    position: absolute; left: 0; right: 0; text-align: center;
    font-weight: 600; font-size: 30px; letter-spacing: 4px; text-transform: uppercase;
    color: var(--brand-blue);
  }
  .card-front .brand-name { top: 76px; }
  .card-back .brand-name { top: 56px; color: var(--card-white); }

  .person { position: absolute; right: 365px; top: 196px; text-align: right; }
  .person-name { font-weight: 700; font-size: 30px; line-height: 36px; color: var(--brand-blue); letter-spacing: 0.3px; }
  .person-role { font-weight: 700; font-size: 20px; line-height: 26px; color: var(--ink); }

  .divider { position: absolute; left: 337px; top: 197px; width: 2px; height: 64px; background: var(--brand-blue); }

  .contacts { position: absolute; left: 355px; top: 193px; list-style: none; }
  .contacts li {
    display: flex; align-items: center; gap: 7px;
    font-size: 18px; line-height: 23px; color: var(--ink);
  }
  .contacts svg { width: 14px; height: 14px; fill: var(--brand-blue); flex: none; }

  .address {
    position: absolute; left: 0; right: 0; top: 295px; text-align: center;
    font-size: 18px; color: var(--ink);
  }
  .wave { position: absolute; left: 0; top: 0; width: 680px; height: 392px; }

  .backdrop-photo {
    position: absolute; inset: 0;
    background:
      linear-gradient(180deg, rgba(255,255,255,0) 65%, rgba(40,70,110,0.25) 100%),
      linear-gradient(160deg, var(--photo-mid) 0%, var(--photo-light) 45%, var(--photo-deep) 100%);
  }
</style>
</head>
<body>
<main class="canvas">
  <section class="card card-front">
    <svg class="wave" viewBox="0 0 680 392" preserveAspectRatio="none" aria-hidden="true">
      <path d="M0 329 Q340 414 680 329 L680 392 L0 392 Z" fill="var(--brand-blue)"/>
      <path d="M0 312 Q340 400 680 312 Q340 410 0 312 Z" fill="var(--accent-grey)"/>
    </svg>
    <div class="brand-name">Ashford Crest Senior Living</div>
    <div class="person">
      <div class="person-name">DANIEL HARPER</div>
      <div class="person-role">OWNER</div>
    </div>
    <div class="divider"></div>
    <ul class="contacts">
      <li>
        <svg viewBox="0 0 16 16"><path d="M2 6c0-2 2-3 6-3s6 1 6 3v1h-3V5.5H5V7H2z M4 8h8l1.5 5h-11z M8 9.2a1.6 1.6 0 1 0 0.01 0z"/></svg>
        (555) 014-2870
      </li>
      <li>
        <svg viewBox="0 0 16 16"><path d="M1 3h14v10H1z" fill="none" stroke="var(--brand-blue)" stroke-width="1.6"/><path d="M1 3l7 6 7-6" fill="none" stroke="var(--brand-blue)" stroke-width="1.6"/></svg>
        hello@ashfordcrest.com
      </li>
      <li>
        <svg viewBox="0 0 16 16"><circle cx="8" cy="8" r="6.5" fill="none" stroke="var(--brand-blue)" stroke-width="1.5"/><path d="M1.5 8h13M8 1.5c-3 3.5-3 9.5 0 13M8 1.5c3 3.5 3 9.5 0 13" fill="none" stroke="var(--brand-blue)" stroke-width="1.2"/></svg>
        www.ashfordcrest.com
      </li>
    </ul>
    <p class="address">4200 Maple Row Ave. Pasadena, CA 91101</p>
  </section>

  <section class="card card-back">
    <div class="backdrop-photo" role="img" aria-label="Blue-tinted photograph of an elderly couple seen from behind, sitting on a park bench among autumn trees"></div>
    <div class="brand-name">Ashford Crest Senior Living</div>
  </section>
</main>
</body>
</html>
```